Update Old OR create new Website

Current Website is looking a bit old, I did this one a few years back.

Would like a fresh new look, current website sitepress theme is " the Vanta theme" from plumcrate and I just purchased this theme - "bravlo" also from plumcrate, I quite like the look of - http://bravlo.quorvex-skins.com/tech-business/ and if we could get somthing simlar would be great.

current website is at http://www.hle.com.au, have been playing around with the slider that i like.

I have said 5 pages to be designed but really it is just a 5 page website where most pages will look the same.

Any questions please let me know

Target Market(s)

Business

Coding

Coded - Design and coding required

Number of Pages Required

5+ page

Font styles to use
Sans Serif

Colors
33a6d7
0292cd
ffffff
0255a3

Requirements
Must have
• Device compatibility - pc, tablet, phone
Nice to have
• video
Should not have
• vunerabilities. Must also use images that will expire or disappear, ie must be uploaded to site not links to elsewhere.

```html
<!DOCTYPE html>
<html lang="en">
<head>
<meta charset="utf-8">
<title>Quillon Technologies</title>
<link href="https://fonts.googleapis.com/css2?family=Montserrat:wght@400;500;600;700&family=Open+Sans:wght@400;600;700&display=swap" rel="stylesheet">
<style>
:root{
  --blue:#1fb0e3;
  --blue-mid:#0292cd;
  --blue-soft:#33a6d7;
  --blue-deep:#0255a3;
  --ink:#222;
  --text:#555;
  --white:#fff;
  --dark:#3c3c3c;
  --darker:#2b2b2b;
  --footer:#262626;
  --footer-bar:#1a1a1a;
  --grey-bg:#f1f1f1;
  --line:#e3e3e3;
}
*{box-sizing:border-box;margin:0;padding:0}
html,body{width:1200px;height:3982px;overflow:hidden}
body{position:relative;font-family:"Open Sans",Arial,sans-serif;color:var(--text);background:var(--white)}
.abs{position:absolute}
section,header,nav,footer{position:absolute;left:0;width:1200px}
h2.section-title{position:absolute;left:0;width:1200px;text-align:center;font-family:"Montserrat",Arial,sans-serif;font-weight:500;font-size:38px;color:var(--ink)}
.section-lead{position:absolute;left:270px;width:660px;text-align:center;font-size:13px;line-height:20px;color:#666}

/* header */
.site-header{top:0;height:125px;background:var(--white)}
.brand{left:80px;top:40px;display:flex;align-items:center;gap:12px}
.brand-mark{width:40px;height:40px;background:var(--blue)}
.brand-name{font-family:"Montserrat",Arial,sans-serif;font-weight:600;font-size:24px;color:#333}
.contact-item{top:38px;display:flex;gap:12px;align-items:flex-start}
.contact-icon{width:28px;height:28px;border-radius:50%;background:var(--blue);display:flex;align-items:center;justify-content:center}
.contact-item p{font-size:12px;line-height:16px;color:#333}
.contact-item strong{font-weight:700}

/* nav */
.main-nav{top:125px;height:43px;background:var(--blue)}
.main-nav a{position:absolute;top:13px;font-family:"Montserrat",Arial,sans-serif;font-size:12.5px;font-weight:600;color:var(--white);text-decoration:none;letter-spacing:.3px}
.social-tab{left:960px;top:-18px;width:240px;height:48px;background:#555;clip-path:polygon(24px 0,100% 0,100% 100%,0 100%);display:flex;gap:9px;align-items:center;padding-left:42px}
.social-tab span{width:26px;height:26px;border-radius:50%;border:2px solid var(--white)}

/* hero */
.hero{top:168px;height:456px;background:linear-gradient(120deg,#4a4d52 0%,#2f3236 45%,#5a5d61 100%)}
.hero h1{position:absolute;left:82px;top:116px;width:580px;font-family:"Montserrat",Arial,sans-serif;font-weight:700;font-size:32px;line-height:42px;color:var(--white)}
.hero p{position:absolute;left:84px;top:222px;font-size:17px;color:var(--white)}
.btn{display:inline-flex;align-items:center;justify-content:center;background:var(--blue);color:var(--white);font-weight:600;text-decoration:none}
.hero .btn{position:absolute;left:84px;top:276px;width:142px;height:42px;border-radius:21px;font-size:14px}
.hero-visual{left:694px;top:118px;width:396px;height:338px;background:linear-gradient(160deg,#f6f8fa,#d8e4ec);border-radius:14px 14px 0 0}
.hero-dots{left:552px;top:413px;display:flex;gap:9px}
.hero-dots span{width:9px;height:9px;border-radius:50%;background:var(--white)}
.hero-dots span:first-child{background:var(--blue)}

/* who we are */
.who{top:624px;height:558px;background:var(--dark)}
.who h2.section-title{top:48px;color:var(--white)}
.who .section-lead{top:108px;color:#ccc}
.who-card{position:absolute;top:200px;width:260px;text-align:center;color:var(--white)}
.who-card .icon{width:132px;height:132px;border-radius:50%;margin:0 auto;border:8px solid #666;display:flex;align-items:center;justify-content:center}
.who-card .icon i{display:block;width:62px;height:62px;border-radius:12px;background:rgba(255,255,255,.85)}
.who-card h3{font-family:"Montserrat",Arial,sans-serif;font-weight:500;font-size:17px;margin-top:26px}
.who-card p{font-size:12.5px;line-height:16px;color:#ddd;margin:12px auto 0;width:210px}
.who-card.active{top:198px;left:584px;height:394px;background:var(--darker);border-top:8px solid var(--blue);padding-top:32px}
.who-card.active .btn{position:absolute;left:12px;bottom:12px;width:236px;height:58px;font-size:14px}
.arrow{position:absolute;top:290px}

/* services */
.services{top:1182px;height:783px;background:var(--white)}
.services h2.section-title{top:112px;font-size:40px}
.services .section-lead{top:172px}
.service{position:absolute;width:330px}
.service h3{font-family:"Montserrat",Arial,sans-serif;font-weight:500;font-size:21px;color:var(--ink)}
.service p{font-size:13px;line-height:17px;color:#444;margin-top:14px}
.service .sicon{position:absolute;top:-8px;width:46px;height:46px;border-radius:8px;background:var(--blue);display:flex;align-items:center;justify-content:center}
.service.left{left:84px}
.service.left .sicon{left:278px}
.service.right{left:794px}
.service.right h3{padding-left:0}
.service.right .sicon{left:-58px}
.service-figure{left:460px;top:305px;width:270px;height:400px;background:linear-gradient(180deg,#f0f3f6,#c9d3dc 70%,#eef1f4);border-radius:6px}

/* pricing */
.pricing{top:1965px;height:743px;background:#f4f4f4}
.pricing h2.section-title{top:62px}
.plan{position:absolute;top:172px;width:222px;height:497px;background:var(--white);border:1px solid #cfe4ef;border-top:7px solid var(--blue);text-align:center;font-size:12px;color:#333}
.plan h4{height:46px;line-height:42px;font-family:"Montserrat",Arial,sans-serif;font-weight:600;font-size:14px;border-bottom:1px solid var(--line)}
.plan .gets{height:68px;line-height:68px;font-size:15px;color:#666;border-bottom:1px solid var(--line)}
.plan li{list-style:none;height:42px;line-height:42px;border-bottom:1px solid var(--line)}
.plan li:nth-child(even){background:#f7f7f7}
.plan .btn{display:flex;height:48px;font-size:16px;margin:0}
.plan .price{position:absolute;left:0;bottom:10px;width:100%;line-height:18px}
.plan .price b{font-family:"Montserrat",Arial,sans-serif;font-size:22px;font-weight:600}
.plan .price small{display:block;font-size:12px}
.plan.featured{background:var(--blue);color:var(--white);border-color:var(--blue)}
.plan.featured h4,.plan.featured .gets{background:#5bc6ea;color:#e7f6fc;border-color:#49bde5}
.plan.featured li{background:#13a3d6;border-color:#36b6e2}
.plan.featured li:nth-child(even){background:#0b8fc0}
.plan.featured .spacer{height:48px}

/* video */
.video{top:2708px;height:438px;background:#efefef}
.video h2{position:absolute;left:86px;top:74px;font-family:"Montserrat",Arial,sans-serif;font-weight:500;font-size:31px;color:var(--ink)}
.video .intro{position:absolute;left:86px;top:128px;width:450px;font-size:13px;line-height:18px;font-weight:700;color:#333}
.video .body{position:absolute;left:86px;top:186px;width:450px;font-size:13px;line-height:19px;color:#666}
.video .btn{position:absolute;left:86px;top:300px;width:148px;height:48px;font-size:14px}
.video-frame{left:566px;top:53px;width:544px;height:324px;background:radial-gradient(circle at 50% 55%,#5b5b5b,#2d2d2d 75%)}
.play{left:810px;top:188px}

/* testimonials */
.testimonials{top:3146px;height:486px;background:var(--white)}
.testimonials h2.section-title{top:62px}
.quote{position:absolute;width:428px;height:126px;padding:24px 30px;font-size:14px;line-height:22px;color:var(--white);text-align:center}
.quote::after{content:"";position:absolute;bottom:-22px;width:0;height:0;border-top:22px solid currentColor;border-left:22px solid transparent}
.quote.one{left:175px;top:159px;background:#2d96c8}
.quote.one::after{right:120px;color:#2d96c8}
.quote.two{left:581px;top:186px;background:#2e2e2e;border:2px solid #fff}
.quote.two::after{left:30px;color:#2e2e2e}
.author{position:absolute;display:flex;align-items:center;gap:12px}
.author .avatar{width:40px;height:40px;border-radius:50%;background:#9aa3ab}
.author b{display:block;font-size:14px;font-weight:600;color:#333}
.author small{font-size:11px;color:#999}
.nav-circle{position:absolute;top:259px;width:42px;height:42px;border-radius:50%;border:1px solid #ddd}

/* footer */
.site-footer{top:3632px;height:318px;background:var(--footer);color:#bbb}
.site-footer h5{position:absolute;top:46px;font-family:"Montserrat",Arial,sans-serif;font-size:13px;font-weight:600;color:var(--white);letter-spacing:.5px}
.f-brand{left:98px;top:54px;display:flex;align-items:center;gap:10px}
.f-brand span:first-child{width:32px;height:32px;background:var(--blue)}
.f-brand span:last-child{font-family:"Montserrat",Arial,sans-serif;font-weight:600;font-size:18px;color:var(--white)}
.f-about{left:98px;top:128px;width:190px;font-size:11px;line-height:17px}
.f-social{left:98px;top:226px;display:flex;gap:10px}
.f-social span{width:26px;height:26px;border-radius:50%;background:#666}
.f-list{position:absolute;list-style:none;font-size:11px;line-height:16px}
.f-list li{display:flex;gap:10px;align-items:flex-start;margin-bottom:15px}
.f-list i{display:block;flex:0 0 10px;height:10px;margin-top:3px;border-radius:50%;background:var(--blue)}
.f-links li{margin-bottom:17px}
.f-links li::before{content:"›";margin-right:8px;color:#888}
.news p{position:absolute;left:871px;top:86px;width:240px;font-size:11px;line-height:18px}
.news .field{position:absolute;left:871px;top:162px;width:230px;height:40px;border:1px solid #555;padding:11px 14px;font-size:12px;color:#ccc}
.news .btn{position:absolute;left:871px;top:227px;width:230px;height:40px;font-size:13px}
.footer-bar{top:3950px;height:32px;background:var(--footer-bar);text-align:center;line-height:32px;font-size:11px;color:#aaa}
</style>
</head>
<body>

<header class="site-header">
  <div class="abs brand"><span class="brand-mark"></span><span class="brand-name">Quillon Technologies</span></div>
  <div class="abs contact-item" style="left:512px">
    <span class="contact-icon"><svg width="14" height="16" viewBox="0 0 14 16"><path d="M7 0a6 6 0 0 0-6 6c0 4.5 6 10 6 10s6-5.5 6-10a6 6 0 0 0-6-6zm0 8.5A2.5 2.5 0 1 1 7 3.5a2.5 2.5 0 0 1 0 5z" fill="#fff"/></svg></span>
    <p>418 Harlow Avenue, Suite 12<br>Brookfield</p>
  </div>
  <div class="abs contact-item" style="left:752px">
    <span class="contact-icon"><svg width="14" height="14" viewBox="0 0 14 14"><path d="M3 1l2 3-1.3 1.6a8 8 0 0 0 4.7 4.7L10 9l3 2-1 2.5C6 13.5.5 8 .5 2z" fill="#fff"/></svg></span>
    <p><strong>Call Us</strong><br>(555) 318-0472</p>
  </div>
  <div class="abs contact-item" style="left:924px">
    <span class="contact-icon"><svg width="15" height="11" viewBox="0 0 15 11"><rect x=".5" y=".5" width="14" height="10" fill="none" stroke="#fff"/><path d="M.5.5l7 5 7-5" fill="none" stroke="#fff"/></svg></span>
    <p><strong>Email Address</strong><br>hello@quillontech.com</p>
  </div>
</header>

<nav class="main-nav">
  <a href="#" style="left:106px">HOME</a>
  <a href="#" style="left:196px">ABOUT US</a>
  <a href="#" style="left:316px">WHAT WE DO</a>
  <a href="#" style="left:452px">OUR SERVICES</a>
  <a href="#" style="left:600px">OUR PORTFOLIO</a>
  <a href="#" style="left:760px">BLOG</a>
  <a href="#" style="left:846px">CONTACT US</a>
  <div class="abs social-tab"><span></span><span></span><span></span><span></span><span></span><span></span></div>
</nav>

<section class="hero">
  <h1>Quillon Technologies Quality Web Design &amp; Development</h1>
  <p>One stop for all your website requirements</p>
  <a class="btn" href="#">Learn More</a>
  <div class="abs hero-visual" role="img" aria-label="Tablet and phone mockups showing a pie chart website layout"></div>
  <div class="abs hero-dots"><span></span><span></span><span></span><span></span></div>
</section>

<section class="who">
  <h2 class="section-title">Who We Are</h2>
  <p class="section-lead">vestibulum ullamcorper, mi sit amet malesuada porttitor, justo tortor sodales lectus, eget fringilla nulla dui et sem. Vivamus ac tincidunt lacusmauris gravida.</p>
  <svg class="arrow" style="left:46px" width="16" height="30" viewBox="0 0 16 30"><path d="M14 2L2 15l12 13" fill="none" stroke="#fff" stroke-width="2"/></svg>
  <svg class="arrow" style="left:1140px" width="16" height="30" viewBox="0 0 16 30"><path d="M2 2l12 13L2 28" fill="none" stroke="#fff" stroke-width="2"/></svg>
  <div class="who-card" style="left:70px"><div class="icon" style="background:#5a9ad6"><i></i></div><h3>Adroid Application</h3><p>It has survived not only five centuries, but also the leap into electronic typesetting, remaining essentially unchanged.</p></div>
  <div class="who-card" style="left:322px"><div class="icon" style="background:#f2c84b"><i></i></div><h3>Web Development</h3><p>It has survived not only five centuries, but also the leap into electronic typesetting, remaining essentially unchanged.</p></div>
  <div class="who-card active"><div class="icon" style="background:#3aa7e0;border-color:#fff"><i></i></div><h3>Web Designing</h3><p>It has survived not only five centuries, but also the leap into electronic typesetting, remaining essentially unchanged.</p><a class="btn" href="#">READ MORE</a></div>
  <div class="who-card" style="left:870px"><div class="icon" style="background:#f07b5e"><i></i></div><h3>SEO</h3><p>It has survived not only five centuries, but also the leap into electronic typesetting, remaining essentially unchanged.</p></div>
</section>

<section class="services">
  <h2 class="section-title">We Offer Services That Work</h2>
  <p class="section-lead">vestibulum ullamcorper, mi sit amet malesuada porttitor, justo tortor sodales lectus, eget fringilla nulla dui et sem. Vivamus ac tincidunt lacusmauris gravida.</p>

  <div class="service left" style="top:320px"><h3>Local Search Strategy</h3><p>Maximize your presence on search engine results pages on a local scale(very important).</p>
    <span class="sicon"><svg width="22" height="22" viewBox="0 0 22 22"><circle cx="9" cy="9" r="6.5" fill="none" stroke="#fff" stroke-width="2.2"/><path d="M14 14l6 6" stroke="#fff" stroke-width="2.4"/></svg></span></div>
  <div class="service left" style="top:458px"><h3>Maps Search Otimizaion</h3><p>Maximize your presence on search engine results pages on a local scale(very important).</p>
    <span class="sicon"><svg width="16" height="22" viewBox="0 0 16 22"><path d="M8 1a7 7 0 0 0-7 7c0 5 7 13 7 13s7-8 7-13a7 7 0 0 0-7-7z" fill="none" stroke="#fff" stroke-width="2"/><circle cx="8" cy="8" r="2.5" fill="#fff"/></svg></span></div>
  <div class="service left" style="top:592px"><h3>Link Building &amp; Content</h3><p>Maximize your presence on search engine results pages on a local scale(very important).</p>
    <span class="sicon"><svg width="20" height="22" viewBox="0 0 20 22"><rect x="2" y="1" width="16" height="20" fill="none" stroke="#fff" stroke-width="2"/><path d="M6 7h8M6 11h8M6 15h5" stroke="#fff" stroke-width="2"/></svg></span></div>

  <div class="abs service-figure" role="img" aria-label="Photo of a cheering man sitting with a laptop"></div>

  <div class="service right" style="top:320px"><h3>Paid Search Advertising</h3><p>Maximize your presence on search engine results pages on a local scale(very important).</p>
    <span class="sicon"><svg width="22" height="20" viewBox="0 0 22 20"><rect x="1" y="5" width="20" height="14" fill="none" stroke="#fff" stroke-width="2"/><path d="M7 5V1h8v4" fill="none" stroke="#fff" stroke-width="2"/></svg></span></div>
  <div class="service right" style="top:458px"><h3>Custom Website Design</h3><p>Maximize your presence on search engine results pages on a local scale(very important).</p>
    <span class="sicon"><svg width="22" height="20" viewBox="0 0 22 20"><rect x="1" y="1" width="20" height="18" fill="none" stroke="#fff" stroke-width="2"/><path d="M1 6h20" stroke="#fff" stroke-width="2"/></svg></span></div>
  <div class="service right" style="top:592px"><h3>Custom Email Design</h3><p>Maximize your presence on search engine results pages on a local scale(very important).</p>
    <span class="sicon"><svg width="22" height="18" viewBox="0 0 22 18"><rect x="1" y="1" width="20" height="16" fill="none" stroke="#fff" stroke-width="2"/><path d="M1 1l10 8 10-8" fill="none" stroke="#fff" stroke-width="2"/></svg></span></div>
</section>

<section class="pricing">
  <h2 class="section-title">Pricing Tables &amp; Other Features</h2>
  <div class="plan" style="left:117px">
    <h4>1 USER</h4><div class="gets">EACH USER GETS:</div>
    <ul><li><b>Unlimited</b> US+CAN calls*</li><li><b>Free</b> IP Desk Phone</li><li>local or toll-free number</li><li><b>150</b> toll free minutes</li><li>Over <b>30</b> free features</li><li><b>Free</b> set up</li></ul>
    <a class="btn" href="#">Start Trail</a>
    <div class="price"><b>$12.99</b><small>300 min Per month</small></div>
  </div>
  <div class="plan" style="left:366px">
    <h4>2-15 USERS</h4><div class="gets">EACH USER GETS:</div>
    <ul><li><b>Unlimited</b> US+CAN calls*</li><li><b>Free</b> IP Desk Phone</li><li>local or toll-free number</li><li><b>150</b> toll free minutes</li><li>Over <b>30</b> free features</li><li><b>Free</b> set up</li></ul>
    <a class="btn" href="#">Start Trail</a>
    <div class="price"><b>$12.99</b><small>300 min Per month</small></div>
  </div>
  <div class="plan featured" style="left:616px">
    <h4>16-25 USERS</h4><div class="gets">EACH USER GETS:</div>
    <ul><li><b>Unlimited</b> US+CAN calls*</li><li><b>Free</b> IP Desk Phone</li><li>local or toll-free number</li><li><b>150</b> toll free minutes</li><li>Over <b>30</b> free features</li><li><b>Free</b> set up</li></ul>
    <div class="spacer"></div>
    <div class="price"><b>$12.99</b><small>300 min Per month</small></div>
  </div>
  <div class="plan" style="left:871px">
    <h4>16-25 USERS</h4><div class="gets">EACH USER GETS:</div>
    <ul><li><b>Unlimited</b> US+CAN calls*</li><li><b>Free</b> IP Desk Phone</li><li>local or toll-free number</li><li><b>150</b> toll free minutes</li><li>Over <b>30</b> free features</li><li><b>Free</b> set up</li></ul>
    <div class="price"><b>$12.99</b><small>300 min Per month</small></div>
  </div>
</section>

<section class="video">
  <h2>WATCH OUR VIDEO</h2>
  <p class="intro">Lorem ipsum dolor sit amet, nunc mi eget, augue nec integer amet et, luctus eu cras curabitur.</p>
  <p class="body">ut orci eget orci suspendisse autem sem rutrum libero. Ullamcorper suspendisse suspendisse mollis iaculis lobortis ridiculus, vitae a porttitor urna, consectetuer semper at ullamcorper, nunc aenean lobortis wisi tempus. Ac montes.</p>
  <a class="btn" href="#">READ MORE</a>
  <div class="abs video-frame" role="img" aria-label="Video still of a world map with connected people network"></div>
  <svg class="abs play" width="54" height="54" viewBox="0 0 54 54"><circle cx="27" cy="27" r="24" fill="none" stroke="#fff" stroke-width="3"/><path d="M21 16l17 11-17 11z" fill="#fff"/></svg>
</section>

<section class="testimonials">
  <h2 class="section-title">Client Testimonials</h2>
  <span class="nav-circle" style="left:88px"></span>
  <span class="nav-circle" style="left:1076px"></span>
  <div class="quote one">Lorem ipsum dolor sit amet, consectetur adipisicing elit. Enim, delectus atque odit esse harum! Saepe!</div>
  <div class="author" style="left:202px;top:320px"><span class="avatar" role="img" aria-label="Client portrait"></span><div><b>John Doe</b><small>Web designer</small></div></div>
  <div class="quote two">Lorem ipsum dolor sit amet, consectetur adipisicing elit. Enim, delectus atque odit esse harum! Saepe!</div>
  <div class="author" style="left:606px;top:340px"><span class="avatar" role="img" aria-label="Client portrait"></span><div><b>Jessica Doe</b><small>Developer</small></div></div>
</section>

<footer class="site-footer">
  <div class="abs f-brand"><span></span><span>Quillon Technologies</span></div>
  <p class="abs f-about">Brightmere Works is a registered builder and member of the Larkfield Valley Builders Guild.</p>
  <div class="abs f-social"><span></span><span></span><span></span><span></span></div>

  <h5 style="left:356px">GET IN TOUCH</h5>
  <ul class="f-list" style="left:356px;top:86px;width:200px">
    <li><i></i><span>77 Orchard Lane, Fairbay 20418<br>Eastland</span></li>
    <li><i></i><span>0555 7201934</span></li>
    <li><i></i><span>mail@quillontech.com</span></li>
    <li><i></i><span>0555 7201934</span></li>
    <li><i></i><span>Mon - Sat : 9.00 - 18.00</span></li>
  </ul>

  <h5 style="left:613px">INFORMATION</h5>
  <ul class="f-list f-links" style="left:613px;top:88px">
    <li>Home</li><li>About Us</li><li>Our Services</li><li>What We Do</li><li>Contact Us</li>
  </ul>

  <h5 style="left:871px">NEWS LETTER</h5>
  <div class="news">
    <p>Enter your email address for our mailing list to keep your self our hottest updated.</p>
    <div class="field">Email</div>
    <a class="btn" href="#">Sign up</a>
  </div>
</footer>
<div class="abs footer-bar" style="left:0;width:1200px">Copyright © 2017 www.quillontech.com, All Rights Reserved</div>

</body>
</html>
```